Australian Painting company requires DL Flyer to help grow business

We need a flyer to post, email and leave with clients which details our company information and identifies the services we provide

Needs to incorporate our existing logo and show photos which will be provided when basic layout and designer is chosen

my mistake for not making the brief clear earlier; I would like an A4 double sided flyer which folds to DL

Target Market(s)

property managers, facility managers, property owners

Industry/Entity Type

Business

Requirements
Must have
• Company Name - Bellwick Paintworks Australia
Phone Number - 1300 842 306
Web Address - www.bpwks.com.au
Email: admin@bpwks.com.au
Facebook symbol
Twitter symbol
Logo - Attached to brief
Description of services;
◾External Painting
◾Internal Painting
◾Texture Coating
◾Two Pak Epoxy products
◾Line marking
◾Epoxy floors and walkways
◾Waterproofing
◾Roof Painting
◾Handyman Services
◾Rope Access Painting
◾Maintenance Programmes
◾Painting Project Management
◾Prestigious Home Painting
Nice to have
• Photos of some projects; some photos are attached
can provide more when a design is selected
Should not have
• Too much information - needs to be easy to read

```html
<!DOCTYPE html>
<html lang="en">
<head>
<meta charset="utf-8">
<title>Bellwick Paintworks Australia – Services Flyer</title>
<link rel="stylesheet" href="https://fonts.googleapis.com/css2?family=Open+Sans:wght@400;700&family=Ubuntu:wght@400;500&display=swap">
<style>
  :root {
    --canvas-bg: #eef2f4;
    --paper: #ffffff;
    --ink: #1d1d1f;
    --ink-soft: #444448;
    --white: #ffffff;
    --haze-blue: #e3f1f8;
    --haze-peach: #fbe4d4;
    --pink-light: #f6a6cb;
    --pink: #ee3f93;
    --magenta: #e8237a;
    --coral: #f25a45;
    --fold-shadow: rgba(0, 0, 0, 0.10);
    --strip-fill: rgba(255, 255, 255, 0.16);
    --strip-line: rgba(255, 255, 255, 0.35);
    --social-dot: rgba(255, 255, 255, 0.9);
  }
  * { box-sizing: border-box; margin: 0; padding: 0; }
  html, body {
    width: 1137px; height: 1200px; overflow: hidden;
    background: var(--canvas-bg);
  }
  .canvas { position: relative; width: 1137px; height: 1200px; }
  .spread {
    position: absolute; left: 128px; top: 32px;
    width: 880px; height: 1136px;
    background: var(--paper);
    box-shadow: 0 6px 24px rgba(0,0,0,0.18);
    overflow: hidden;
    font-family: "Ubuntu", sans-serif;
    color: var(--ink);
  }
  .spread-backdrop {
    position: absolute; inset: 0;
    background: linear-gradient(180deg,
      var(--paper) 0%, var(--paper) 46%,
      var(--haze-blue) 57%, var(--haze-peach) 66%,
      var(--pink-light) 72%, var(--pink) 81%,
      var(--magenta) 90%, var(--coral) 100%);
  }
  .fold {
    position: absolute; left: 440px; top: 0; width: 24px; height: 100%;
    background: linear-gradient(90deg, transparent, var(--fold-shadow) 45%, transparent);
  }
  .abs { position: absolute; }

  .brand { left: 54px; top: 66px; display: flex; align-items: center; gap: 10px; }
  .brand-mark { width: 14px; height: 14px; background: var(--ink); }
  .brand-name { font-family: "Open Sans", sans-serif; font-weight: 700; font-size: 17px; letter-spacing: 0.5px; color: var(--ink); }

  .about-title { left: 54px; top: 134px; font-size: 29px; font-weight: 400; }
  .about-copy { left: 54px; top: 180px; width: 330px; font-family: "Open Sans", sans-serif; font-size: 15px; line-height: 20.5px; color: var(--ink-soft); }
  .about-copy p + p { margin-top: 20px; }

  .photo { position: absolute; width: 182px; height: 120px; }
  .photo-house { background: linear-gradient(180deg, #8fc4ee 0%, #e9b94c 55%, #6f9a3a 100%); }
  .photo-interior { background: linear-gradient(120deg, #7b6a2c 0%, #d8cb63 55%, #a9b8c2 100%); }
  .photo-roller { background: radial-gradient(ellipse at 50% 45%, #e8ddc8 0%, #cdbfa5 70%, #b9aa8e 100%); }
  .photo-lines { background: linear-gradient(180deg, #c9c9c7 0%, #3f8fd0 25%, #c9c9c7 40%, #3f8fd0 62%, #c9c9c7 78%, #b6b6b4 100%); }
  .photo-floor { background: linear-gradient(180deg, #2d2f36 0%, #a84c2a 35%, #c8d0d6 60%, #6e7f8c 100%); }
  .photo-wall { background: linear-gradient(100deg, #8f8f8f 0%, #e6e6e6 40%, #f2f2f2 100%); }

  .service { font-size: 28px; line-height: 36px; font-weight: 400; }
  .service-small { font-size: 23px; line-height: 25px; font-weight: 400; }

  .strip {
    position: absolute; left: 466px; width: 414px;
    background: var(--strip-fill);
    border-top: 1px solid var(--strip-line);
    border-left: 1px solid var(--strip-line);
    border-radius: 4px 0 0 4px;
  }

  .cta {
    font-family: "Open Sans", sans-serif; font-weight: 700;
    font-size: 54px; line-height: 1; color: var(--white);
    text-shadow: 0 2px 6px rgba(120, 0, 60, 0.35);
  }

  .contact-line {
    left: 0; top: 1104px; width: 880px;
    display: flex; justify-content: center; align-items: center; gap: 28px;
    font-family: "Open Sans", sans-serif; font-size: 15px; color: var(--white);
  }
  .social { display: flex; gap: 8px; }
  .social-dot { width: 16px; height: 16px; border-radius: 50%; background: var(--social-dot); }
</style>
</head>
<body>
<main class="canvas">
  <article class="spread">
    <div class="spread-backdrop" role="img" aria-label="Soft rainbow colour wash background"></div>
    <div class="fold"></div>

    <!-- Left panel -->
    <div class="abs brand">
      <span class="brand-mark"></span>
      <span class="brand-name">Bellwick Paintworks Australia</span>
    </div>
    <h1 class="abs about-title">About Us</h1>
    <div class="abs about-copy">
      <p>We need a flyer to post, email and leave with clients which details our company information and identifies the services we provide</p>
      <p>Needs to incorporate our existing logo and show photos which will be provided when basic layout and designer is chosen</p>
      <p>my mistake for not making the brief clear earlier; I would like an A4 double sided flyer which folds to DL</p>
    </div>

    <div class="photo photo-house" style="left:45px; top:460px;" role="img" aria-label="Photo of a freshly painted two-storey house exterior"></div>
    <h2 class="abs service" style="left:248px; top:496px;">External<br>Painting</h2>

    <h2 class="abs service" style="left:64px; top:614px;">Internal<br>Painting</h2>
    <div class="photo photo-interior" style="left:210px; top:606px; height:116px;" role="img" aria-label="Photo of a painted interior room"></div>

    <div class="photo photo-roller" style="left:45px; top:746px;" role="img" aria-label="Photo of a texture-coated wall with paint roller"></div>
    <h2 class="abs service" style="left:252px; top:764px;">Texture<br>Coating</h2>

    <h2 class="abs service" style="left:71px; top:894px;">Two Pak<br>Epoxy<br>products</h2>
    <div class="photo photo-roller" style="left:210px; top:893px;" role="img" aria-label="Photo of a two pak epoxy coated surface with paint roller"></div>

    <p class="abs cta" style="left:58px; top:1036px;">Call Us Now</p>

    <!-- Right panel -->
    <div class="photo photo-lines" style="left:497px; top:58px;" role="img" aria-label="Photo of blue line marking on a wall corner"></div>
    <h2 class="abs service" style="left:695px; top:90px;">Line<br>marking</h2>

    <h2 class="abs service" style="left:492px; top:212px;">Epoxy<br>floors &amp;<br>walkways</h2>
    <div class="photo photo-floor" style="left:637px; top:206px;" role="img" aria-label="Photo of an epoxy-coated warehouse floor and walkway"></div>

    <div class="photo photo-wall" style="left:492px; top:358px;" role="img" aria-label="Photo of waterproofing membrane applied to a wall"></div>
    <h2 class="abs service" style="left:692px; top:372px;">Water-<br>proofing</h2>

    <h2 class="abs service" style="left:496px; top:512px;">Roof<br>Painting</h2>
    <div class="photo photo-roller" style="left:637px; top:508px;" role="img" aria-label="Photo of roof painting work"></div>

    <div class="photo photo-roller" style="left:492px; top:653px;" role="img" aria-label="Photo of handyman repair and painting work"></div>
    <h2 class="abs service" style="left:697px; top:674px;">Handyman<br>Services</h2>

    <div class="strip" style="top:800px; height:74px;"></div>
    <div class="strip" style="top:874px; height:72px;"></div>
    <div class="strip" style="top:946px; height:64px;"></div>

    <h2 class="abs service-small" style="left:496px; top:810px;">Rope Access Painting<br>Maintenance Programmes</h2>
    <h2 class="abs service-small" style="left:496px; top:886px;">Painting Project<br>Management</h2>
    <h2 class="abs service-small" style="left:496px; top:966px;">Prestigious Home Painting</h2>

    <p class="abs cta" style="left:504px; top:1038px; font-size:50px;">1300 842 306</p>

    <div class="abs contact-line">
      <span>www.bpwks.com.au</span>
      <span>admin@bpwks.com.au</span>
      <span class="social" aria-label="Social media links">
        <span class="social-dot"></span>
        <span class="social-dot"></span>
      </span>
    </div>
  </article>
</main>
</body>
</html>
```